Halt and Thicken New Branding Stationary Set - updated Oct 30th 2017

Updated on 30th Oct 2017 as we now need a whole folder design instead of a folder cover. We have thought out exactly what should be on it so it wont be hard. We are happy for this to be completed only by the winning designer if you like. And also we are guaranteeing this project now. Thanks!

We just got our new logo and now we would like a stationary set so we can brand our company communications. The items we need designed are:
Business cards
Letterhead
Appointment confirmation cards
Folder - switched from folder cover. Note that if you don't wish to do this unless you are selected as the winner this is fine.

1. Business cards - for 5 employees, final names will be given once the winner is selected, but you can use this one as the sample:
Lucinda Marquez
Hair Regrowth Expert
Halt and Thicken
7182 Oakmere Ave, Suite 500
Beverly Hills CA 90299
lucinda@jamesholloway-md.example
(310) 555-0193

2. Letterhead 8.5" x 11.0" vertical
Halt and Thicken
Beverly Hills CA 90299
office@haltandthicken.example
(310) 555-0193

3. Appointment Confirmation cards - business card size
Halt and Thicken
Beverly Hills CA 90299
Appointment For:
Date:
Time:
If you are unable to make your appointment, please contact us to reschedule at:
(310) 555-0193
info@jamesholloway-md.example

*UPDATED*
4. Folder 9" x 12 " vertical with double pocket
We would like the infinity image from the logo made really big so the left side is on the back and the right side with the + sign is on the front and its takes up the maximum room on the folder.
On the front below the half logo it should say "A Biochemical Revolution..."
On the inside we would also like to have the infinity sign from the logo but faded and half on the left pocket half on the right.
On left inside pocket it should say (this will be partically written on top of the logo):
James Holloway MD
Precision Medicine
Halt and Thicken Hair
On the Right inside pocket it should say the following:
Because the Enemy of BETTER Health is Good Health
BETTER Ingredients
BETTER Recipe
BETTER Medicine
On the back below the logo on the bottom should be the contact information.
I attached a picture of our drawing of what we want for this to make it easier.

Here is our website to give you an idea of our branding: http://www.haltandthicken.example/

We are the only true cure for hair loss and need to look professional and highest quality and beyond reproach from an ethical standpoint. We are a medical clinic so this should be portrayed also.
We cured hair loss by analyzing biochemistry and rebalancing it so that the process reverses and your own hair can grow back naturally.

Business card information:

OK so here is the information for the business cards:

Lucinda Marquez
Hair Regrowth Expert
(310) 555-0193
www.haltandthicken.example

Marisol Quintero
Hair Growth Consultant
(310) 555-0193
marisol@jamesholloway-md.example
www.haltandthicken.example

Janice Pelham
CMO/COO
(310) 555-0193
janice@haltandthicken.example
www.haltandthicken.example

Dr Glen Holloway
President
(310) 555-0193
info@jamesholloway-md.example
www.haltandthicken.example

Halt and Thicken
Customer Service
(310) 555-0193
info@jamesholloway-md.example
www.haltandthicken.example

Target Market(s)

Men aged 20-24 who care about their appearance, care about their hair and care about the world.

Industry/Entity Type

Medical And Science

Font styles to use
Sans Serif

Colors
00a990
ffffff
9d9d9d
333333

Requirements
Must have
• Must use the logo and our brand colors from the logo in all designs.
• The pantone colors are:
• Green: #4ca26f
• Light Grey: #999999
• The design should be symmetrical and balanced.
Nice to have
• It should look reasonably masculine.
Should not have
• Do not include any red in the design.

```html
<!DOCTYPE html>
<html lang="en">
<head>
<meta charset="utf-8">
<title>Halt and Thicken Stationery Set</title>
<link rel="stylesheet" href="https://fonts.googleapis.com/css2?family=Montserrat:wght@400;500;600&family=Open+Sans:wght@400;600&display=swap">
<style>
:root{
  --bg:#e3f0f2;
  --paper:#ffffff;
  --card:#f7f7f7;
  --green:#4aa36c;
  --grey:#9d9d9d;
  --dark:#555555;
  --text:#8a8a8a;
  --line:#9d9d9d;
}
*{box-sizing:border-box;margin:0;padding:0}
html,body{width:1200px;height:1200px;overflow:hidden;background:var(--bg)}
body{position:relative;font-family:"Open Sans",sans-serif;color:var(--text)}
.sheet,.card{position:absolute;background:var(--paper);overflow:hidden}
.card{background:var(--card)}
.abs{position:absolute}
.brand{display:flex;align-items:center;gap:8px;font-family:"Montserrat",sans-serif;font-weight:600;color:var(--green);white-space:nowrap;letter-spacing:-.2px}
.brand .dot{border-radius:50%;background:var(--green);flex:none}
.url{font-family:"Montserrat",sans-serif;color:var(--dark)}
.band{position:absolute;left:0;right:0;background:var(--green)}
.band-text{position:absolute;color:#fff;font-family:"Montserrat",sans-serif;font-weight:500;white-space:nowrap}

/* letterhead */
.letterhead{left:94px;top:102px;width:512px;height:724px}
.letter-body p{font-size:7.6px;line-height:12px;text-align:justify;margin-bottom:6px;color:#8f8f8f}
.recipient{font-family:"Montserrat",sans-serif;color:var(--green);font-size:16px;font-weight:400}
.signature{width:60px;height:14px;background:linear-gradient(90deg,#eeeeee,#f6f6f6);border-radius:2px}

/* folder */
.folder{left:618px;top:102px;width:512px;height:724px}
.title-line{position:absolute;height:1px;background:var(--line)}

/* cards */
.card-brand{left:102px;top:854px;width:320px;height:174px}
.card-person{left:462px;top:854px;width:318px;height:174px}
.card-appt{left:816px;top:856px;width:318px;height:174px}
.small{font-family:"Montserrat",sans-serif;font-size:7.5px;color:#8a8a8a;white-space:nowrap}
</style>
</head>
<body>

<!-- Letterhead -->
<section class="sheet letterhead">
  <div class="abs" style="right:40px;top:40px;text-align:right">
    <div class="brand" style="font-size:15px;justify-content:flex-end"><span class="dot" style="width:12px;height:12px"></span>HALT AND THICKEN</div>
    <div class="url" style="font-size:7.5px;margin-top:4px;margin-right:16px">www.haltandthicken.example</div>
  </div>

  <div class="abs" style="left:45px;top:170px;font-size:8px">To,</div>
  <div class="abs recipient" style="left:45px;top:184px">JOHNDOE</div>
  <div class="abs" style="left:45px;top:203px;font-size:8px">DESIGNER</div>
  <div class="abs" style="left:375px;top:170px;font-size:7.5px">Date : 01-01-2000</div>

  <div class="abs letter-body" style="left:48px;top:238px;width:420px">
    <p>Lorem Ipsum is simply dummy text of the printing and typesetting industry. Lorem Ipsum has been the industry's standard dummy text ever since the 1500s, when an unknown printer took a galley of type and scrambled it to make a type specimen book. It has survived not only five centuries, but also the leap into electronic typesetting, remaining essentially unchanged. It was popularised in the 1960s with the release of Typeleaf sheets containing Lorem Ipsum passages, and more recently with desktop publishing software like Quillset Composer including versions of Lorem Ipsum.</p>
    <p>Lorem Ipsum is simply dummy text of the printing and typesetting industry. Lorem Ipsum has been the industry's standard dummy text ever since the 1500s, when an unknown printer took a galley of type and scrambled it to make a type specimen book. It has survived not only five centuries, but also the leap into electronic typesetting, remaining essentially unchanged. It was popularised in the 1960s with the release of Typeleaf sheets containing Lorem Ipsum passages, and more recently with desktop publishing software like Quillset Composer including versions of Lorem Ipsum.</p>
    <p>Lorem Ipsum is simply dummy text of the printing and typesetting industry. Lorem Ipsum has been the industry's standard dummy text ever since the 1500s, when an unknown printer took a galley of type and scrambled it to make a type specimen book. It has survived not only five centuries, but also the leap into electronic typesetting, remaining essentially unchanged. It was popularised in the 1960s with the release of Typeleaf sheets containing Lorem Ipsum passages, and more recently with desktop publishing software like Quillset Composer including versions of Lorem Ipsum.</p>
  </div>

  <div class="abs" style="left:70px;top:500px;font-size:7.5px">Sincerely,</div>
  <div class="abs signature" role="img" aria-label="Handwritten signature" style="left:62px;top:513px"></div>
  <div class="abs" style="left:70px;top:530px;font-size:7.5px">Manager</div>

  <div class="brand abs" style="left:26px;top:666px;font-size:11px"><span class="dot" style="width:10px;height:10px"></span>HALT AND THICKEN</div>
  <div class="band" style="top:692px;height:32px"></div>
  <div class="band-text" style="left:150px;top:704px;font-size:6.6px">7182 Oakmere Ave, Suite 500 Beverly Hills CA 90299 &nbsp;|&nbsp; office@haltandthicken.example &nbsp;|&nbsp; (310) 555-0193</div>
</section>

<!-- Folder -->
<section class="sheet folder">
  <div class="abs" style="left:0;right:0;top:160px;display:flex;flex-direction:column;align-items:center">
    <span class="dot" style="display:block;width:78px;height:78px;border-radius:50%;background:var(--green)"></span>
    <div class="brand" style="font-size:34px;margin-top:24px">HALT AND THICKEN</div>
    <div class="url" style="font-size:12px;margin-top:10px">www.haltandthicken.example</div>
  </div>

  <div class="abs" style="left:123px;top:407px;font-size:9px">Title</div>
  <div class="title-line" style="left:144px;width:244px;top:416px"></div>
  <div class="title-line" style="left:142px;width:244px;top:429px"></div>
  <div class="title-line" style="left:142px;width:244px;top:442px"></div>
  <div class="title-line" style="left:142px;width:244px;top:455px"></div>

  <div class="brand abs" style="left:26px;top:666px;font-size:11px"><span class="dot" style="width:10px;height:10px"></span>HALT AND THICKEN</div>
  <div class="band" style="top:692px;height:32px"></div>
  <div class="band-text" style="left:146px;top:704px;font-size:6.6px">7182 Oakmere Ave, Suite 500 Beverly Hills CA 90299 &nbsp;|&nbsp; office@haltandthicken.example &nbsp;|&nbsp; (310) 555-0193</div>
</section>

<!-- Business card front -->
<section class="card card-brand">
  <div class="abs" style="left:0;right:0;top:52px;display:flex;flex-direction:column;align-items:center">
    <div class="brand" style="font-size:17px"><span class="dot" style="width:14px;height:14px"></span>HALT AND THICKEN</div>
    <div class="url" style="font-size:8px;margin-top:12px">www.haltandthicken.example</div>
  </div>
</section>

<!-- Business card back -->
<section class="card card-person">
  <div class="abs" style="left:23px;top:69px;font-family:Montserrat,sans-serif;font-weight:600;font-size:9px;letter-spacing:.8px;color:var(--green)">LUCINDA MARQUEZ</div>
  <div class="abs small" style="left:23px;top:80px">Hair Regrowth Expert</div>
  <div class="abs" style="left:147px;top:54px;width:1px;height:48px;background:var(--line)"></div>
  <div class="abs small" style="left:171px;top:54px;line-height:10px">7182 Oakmere Ave, Suite 500<br>Beverly Hills CA 90299</div>
  <div class="abs small" style="left:171px;top:81px">lucinda@jamesholloway-md.example</div>
  <div class="abs small" style="left:171px;top:96px">(310) 555-0193</div>
  <div class="band" style="top:150px;height:24px"></div>
  <div class="brand abs" style="left:40px;top:134px;font-size:9px;background:var(--card);padding:3px 6px;border-radius:10px"><span class="dot" style="width:8px;height:8px"></span>HALT AND THICKEN</div>
</section>

<!-- Appointment card -->
<section class="card card-appt">
  <div class="abs" style="left:0;right:0;top:14px;display:flex;flex-direction:column;align-items:center">
    <div class="brand" style="font-size:11px"><span class="dot" style="width:9px;height:9px"></span>HALT AND THICKEN</div>
    <div class="url" style="font-size:5.5px;margin-top:4px">www.haltandthicken.example</div>
  </div>
  <div class="abs small" style="left:120px;top:72px">Appointment For:</div>
  <div class="title-line" style="left:32px;width:266px;top:94px;background:#d5d5d5"></div>
  <div class="abs small" style="left:32px;top:100px">Date:</div>
  <div class="title-line" style="left:54px;width:120px;top:108px"></div>
  <div class="abs small" style="left:150px;top:98px">Time:</div>
  <div class="title-line" style="left:172px;width:112px;top:106px"></div>
  <div class="abs small" style="left:130px;top:119px;text-align:center;line-height:9px;font-size:7px">If you are unable to make your appointment,<br>please contact us to reschedule at:</div>
  <div class="abs small" style="left:127px;top:139px;font-size:7px">(310) 555-0193 &nbsp;|&nbsp; info@jamesholloway-md.example</div>
  <div class="band" style="top:154px;height:20px"></div>
  <div class="band-text" style="left:124px;top:160px;font-size:7px">7182 Oakmere Ave. Suite 500 Beverly Hills CA 90299</div>
  <div class="brand abs" style="left:14px;top:147px;font-size:7.5px;background:var(--card);padding:3px 5px;border-radius:10px"><span class="dot" style="width:7px;height:7px"></span>HALT AND THICKEN</div>
</section>

</body>
</html>
```